Kinderbuchverlag sucht Buch-/E-Book-Cover
Zielgruppe
Wir sind ein Kinderbuchverlag. Unsere Zielgruppe sind Kinder, bei diesem Buch im Alter von 3 bis 10 Jahren.
Aufgabenstellung
Das Cover benötige ich für E-book, Taschenbuch und Hardcover Version. Das Cover soll modern passend für Kinder gestalten sein, aber auch Eltern ansprechen. Das Cover soll nach einem hochwertigen Verlags-Cover aussehen und nicht nach einem billigen Publishing Buch. Benutzen Sie moderne Schriften passend für Kinder.
Format:
Print & Hardcover: 13,97 x 21,59 cm (5,5' x 8,5')
Seiten: 76
für Borvell Lesepad
Bitte unser Verlagslogo unten links auf die vordere Seite (Front) mit einfügen.
Buchtitel: Als das Mondlicht im Schneegarten flüstert
Untertitel: Verträumte Erzählungen über flinke Kobolde (Kinderbuch über das Rätsel der Kobolde und ihrer Laternen)
Autor: Henrike L. Bosshammer
Text für die Rückseite des Covers muss drauf:
Ein zauberhafter Blick hinter die Wichteltüren
Ein kräftiges Schneegestöber, ein allzu neugieriger Dackelwelpe und dann auch noch ein Stuhl, der sich einfach nicht reparieren lassen will: Die Weihnachtszeit bei den Menschen stellt die Wichtel vor so manche Herausforderung. Da wird jeder einzelne Tag für Fridolin, Gottfried, Jonte, Paule und ihre Freunde zu einem echten Abenteuer. In sechs spannenden und lustigen Geschichten nimmt dieses Wichtel-Buch die Kinder mit auf eine zauberhafte Reise in die Welt der Wichtel.
Denn diese liebenswerten Gesellen beziehen jedes Jahr - pünktlich zum 1. Dezember - ihre Wohnungen bei den Menschen, stets gut erkennbar an den kleinen Wichteltüren. Bis zum Heiligen Abend begleiten sie 'ihre' Familien, stehen ihnen still und heimlich zur Seite und haben dabei stets nur eines im Sinn: wunderbaren Weihnachtszauber zu verbreiten.
• Dieses Büchlein mit farbigen Illustrationen ist für Kinder von zwei bis acht Jahren geschrieben.
• Diese unterhaltsamen Geschichten eignen sich hervorragend zum Vorlesen, Schulkinder können sich jedoch auch selbst schon daran versuchen.
• Dieses Buch lädt Kinder ein, die Welt..

```html
<!DOCTYPE html>
<html lang="de">
<head>
<meta charset="utf-8">
<title>Als das Mondlicht im Schneegarten flüstert – Buchumschlag</title>
<link href="https://fonts.googleapis.com/css2?family=Amatic+SC:wght@700&family=Roboto:wght@400;700;900&display=swap" rel="stylesheet">
<style>
  :root{
    --wall-dark:#7e1d1f;
    --wall:#9c2a2b;
    --wall-light:#a9413e;
    --board-top:#f4d3d4;
    --board-bottom:#d59a9b;
    --floor:#e3a066;
    --floor-dark:#c9824c;
    --ink:#ffffff;
    --badge:#e89d12;
    --teal:#2ea5c4;
    --gnome:#d3362c;
    --dark:#1d1d1d;
  }
  *{margin:0;padding:0;box-sizing:border-box}
  html,body{width:1200px;height:895px;overflow:hidden;background:#fff}
  .cover{
    position:relative;width:1200px;height:895px;overflow:hidden;
    background:radial-gradient(ellipse at 30% 35%,var(--wall-light) 0%,var(--wall) 45%,var(--wall-dark) 100%);
    color:var(--ink);font-family:"Roboto",sans-serif;
  }
  .baseboard{position:absolute;left:0;right:0;top:652px;height:86px;
    background:linear-gradient(var(--board-top),var(--board-bottom))}
  .floor{position:absolute;left:0;right:0;top:738px;bottom:0;
    background:linear-gradient(var(--floor),var(--floor-dark))}

  /* back */
  .back{position:absolute;left:38px;top:52px;width:505px}
  .back h2{font-family:"Amatic SC",sans-serif;font-weight:700;font-size:29px;letter-spacing:.5px;
    line-height:1;margin-bottom:8px;white-space:nowrap}
  .back p{font-size:12.6px;line-height:20.5px;text-align:justify;margin-bottom:20.5px}
  .back ul{list-style:none;margin-bottom:20.5px;width:470px}
  .back li{font-size:12.6px;line-height:20.5px;padding-left:12px;position:relative}
  .back li::before{content:"•";position:absolute;left:0;font-size:10px}

  /* spine */
  .spine{position:absolute;left:582px;top:0;width:36px;height:660px}
  .spine-title,.spine-author{position:absolute;left:50%;white-space:nowrap;
    transform:translateX(-50%) rotate(-90deg);transform-origin:center}
  .spine-title{top:220px;font-family:"Amatic SC",sans-serif;font-size:21px;letter-spacing:1px}
  .spine-author{top:590px;font-size:17px}

  /* front */
  .front{position:absolute;left:620px;top:0;width:580px;height:895px}
  .author{position:absolute;top:22px;left:0;right:0;text-align:center;font-size:22px;padding-right:40px}
  .title{position:absolute;top:62px;left:0;right:0;text-align:center;
    font-family:"Amatic SC",sans-serif;font-weight:700;line-height:.9}
  .title .small{font-size:50px;display:block}
  .title .huge{font-size:138px;display:block;letter-spacing:2px;margin-top:-8px}
  .title .row{display:flex;align-items:baseline;justify-content:center;gap:10px;margin-top:-6px}
  .title .row .big{font-size:84px}
  .title .row .small{display:inline;font-size:42px}
  .subtitle{position:absolute;top:290px;left:0;right:0;text-align:center;
    font-family:"Amatic SC",sans-serif;font-weight:700;font-size:27px;letter-spacing:.5px}
  .badge{position:absolute;left:36px;top:325px;width:160px;height:160px;border-radius:50%;
    background:var(--badge);display:flex;flex-direction:column;align-items:center;justify-content:center;
    font-family:"Amatic SC",sans-serif;font-weight:700;text-align:center;line-height:.95;transform:rotate(-6deg)}
  .badge .s{font-size:15px}
  .badge .l{font-size:30px}
  .scene{position:absolute;left:168px;top:355px;width:372px;height:470px}
  .publisher{position:absolute;left:23px;top:828px;width:187px;height:67px;background:#fff;
    display:flex;align-items:center;justify-content:center;gap:8px;color:var(--dark);
    font-weight:900;font-size:16px;line-height:1;letter-spacing:.5px;text-transform:uppercase}
  .publisher .mark{width:12px;height:12px;border-radius:50%;background:var(--dark)}
</style>
</head>
<body>
<div class="cover">
  <div class="baseboard"></div>
  <div class="floor"></div>

  <section class="back">
    <h2>Ein zauberhafter Blick hinter die Wichteltüren</h2>
    <p>Ein kräftiges Schneegestöber, ein allzu neugieriger Dackelwelpe und dann auch noch ein Stuhl, der sich einfach nicht reparieren lassen will: Die Weihnachtszeit bei den Menschen stellt die Wichtel vor so manche Herausforderung. Da wird jeder einzelne Tag für Fridolin, Gottfried, Jonte, Paule und ihre Freunde zu einem echten Abenteuer. In sechs spannenden und lustigen Geschichten nimmt dieses Wichtel-Buch die Kinder mit auf eine zauberhafte Reise in die Welt der Wichtel.</p>
    <p>Denn diese liebenswerten Gesellen beziehen jedes Jahr - pünktlich zum 1. Dezember - ihre Wohnungen bei den Menschen, stets gut erkennbar an den kleinen Wichteltüren. Bis zum Heiligen Abend begleiten sie ‚ihre‘ Familien, stehen ihnen still und heimlich zur Seite und haben dabei stets nur eines im Sinn: wunderbaren Weihnachtszauber zu verbreiten.</p>
    <ul>
      <li>Dieses Büchlein mit farbigen Illustrationen ist für Kinder von zwei bis acht Jahren geschrieben.</li>
      <li>Diese unterhaltsamen Geschichten eignen sich hervorragend zum Vorlesen, Schulkinder können sich jedoch auch selbst schon daran versuchen.</li>
      <li>Dieses Buch lädt Kinder ein, die Welt der Wichtel kennenzulernen und verkürzt auf magische Weise die Zeit bis zum Weihnachtsabend</li>
    </ul>
    <p>Die Tradition der Wichteltüren stammt ursprünglich aus Skandinavien, insbesondere in Dänemark ist sie weit verbreitet. Doch auch hierzulande sind immer mehr Menschen von der Magie dieser winzigen Türen fasziniert. Ein Blick dahinter ist den Menschen normalerweise strengstens untersagt. Für die Leser dieses Büchleins jedoch öffnen sich die Wichteltüren einen Spalt breit und gewähren Einblicke in die wundersame Welt dieser liebenswerten Wesen. Es wird spannend und heiter, kurzum: einfach wichtelmäßig magisch ...</p>
  </section>

  <aside class="spine">
    <div class="spine-title">Als das Mondlicht im Schneegarten flüstert</div>
    <div class="spine-author">Henrike L. Bosshammer</div>
  </aside>

  <section class="front">
    <div class="author">Henrike L. Bosshammer</div>
    <h1 class="title">
      <span class="small">Als das</span>
      <span class="huge">Mondlicht</span>
      <span class="row"><span class="small">im</span><span class="big">Schneegarten</span><span class="small">flüstert</span></span>
    </h1>
    <div class="subtitle">Verträumte Erzählungen über flinke Kobolde</div>
    <div class="badge">
      <span class="s">Kinderbuch über das</span>
      <span class="l">Rätsel</span>
      <span class="l">der Kobolde</span>
      <span class="s">und ihrer</span>
      <span class="l">Laternen</span>
    </div>
    <svg class="scene" role="img" aria-label="Illustration: kleine blaue Tür mit Leiter und Briefkasten an der Ziegelwand, davor ein fröhlicher Kobold mit roter Mütze" viewBox="0 0 372 470">
      <defs>
        <linearGradient id="sceneTone" x1="0" y1="0" x2="1" y2="1">
          <stop offset="0" stop-color="#2ea5c4" stop-opacity=".55"/>
          <stop offset="1" stop-color="#d3362c" stop-opacity=".55"/>
        </linearGradient>
      </defs>
      <rect width="372" height="470" rx="10" fill="url(#sceneTone)"/>
    </svg>
    <div class="publisher"><span class="mark"></span><span>Lindenhaus<br>Verlag</span></div>
  </section>
</div>
</body>
</html>
```